UK Online Escort Directory Requires a Redesigned Email Marketing Campaign (4 emails total)

These emails should be designed as marketing emails that will be sent out to approx 10,000 potential customers on a by monthly basis. The designs should be innovative, professional designs that are capable of capturing a readers attention in the blink of an eye.

We have posted this job as our in-house design capabilities are not able to create professional email designs, we therefore require a designer to redesign our email marketing campaign (4 emails total) to a professional level.

The content of the emails will be provided, along with the 5 emails that we are currently sending and the company logo. This should give the potential designer all that they need to redesign the campaign to a professional level.

Please see attached brief for more information on what is required from each individual email.

Target Market(s)

Escorts throughout the UK

Industry/Entity Type

Escort

Font styles to use
Serif
Sans Serif

Requirements
Must have
• Instant recognition of what's being offered.
Nice to have
• Imaginative / inspirational designs.
Should not have
• Any unnecessary wording or text.

```html
<!DOCTYPE html>
<html lang="en">
<head>
<meta charset="utf-8">
<title>Velvet Listings – Profile Email</title>
<link href="https://fonts.googleapis.com/css2?family=Arimo:wght@400;700&display=swap" rel="stylesheet">
<style>
  :root {
    --canvas: #a0a0a0;
    --header-bg: #ffffff;
    --body-bg: #000000;
    --brand: #8a74b8;
    --tagline: #5b6fc4;
    --magenta: #e24ae6;
    --yellow: #f2e632;
    --white: #ffffff;
  }
  * { margin: 0; padding: 0; box-sizing: border-box; }
  html, body { width: 1200px; height: 1000px; overflow: hidden; background: var(--canvas); }
  body { position: relative; font-family: "Arimo", Arial, sans-serif; }

  .email { position: absolute; left: 223px; top: 186px; width: 754px; height: 628px; }

  .email-header { position: absolute; left: 0; top: 0; width: 754px; height: 119px; background: var(--header-bg); }
  .brand-name { position: absolute; left: 79px; top: 26px; font-size: 44px; font-weight: 400; color: var(--brand); white-space: nowrap; }
  .brand-tagline { position: absolute; left: 80px; top: 79px; font-size: 15px; font-weight: 700; color: var(--tagline); }

  .email-body { position: absolute; left: 0; top: 119px; width: 754px; height: 509px; background: var(--body-bg); }

  .profile-frame {
    position: absolute; left: 55px; top: 53px; width: 166px; height: 243px;
    padding: 8px; border-radius: 3px;
    background: linear-gradient(180deg, #ff5a6e 0%, #c84cff 22%, #3ad2ff 50%, #7dff6a 72%, #ffd84a 88%, #ff7a3a 100%);
    box-shadow: 0 0 12px rgba(255, 120, 160, .8), 0 0 18px rgba(120, 200, 255, .5);
  }
  .profile-photo { width: 100%; height: 100%; background: linear-gradient(160deg, #6b5a52 0%, #c99a7a 45%, #e8c49c 65%, #8a6e66 100%); }

  .profile-name { position: absolute; left: 254px; top: 95px; font-size: 30px; font-weight: 700; color: var(--magenta); }
  .profile-location { position: absolute; left: 451px; top: 107px; font-size: 16px; color: var(--yellow); }
  .profile-bio { position: absolute; left: 254px; top: 142px; width: 480px; font-size: 17px; font-weight: 700; line-height: 27.7px; color: var(--white); }

  .cta { position: absolute; font-size: 20px; color: var(--white); white-space: nowrap; }
  .cta a { color: var(--magenta); text-decoration: none; margin-left: 8px; }
  .cta-browse { left: 102px; top: 367px; }
  .cta-browse a { font-size: 22px; letter-spacing: 1px; }
  .cta-post { left: 101px; top: 407px; }
  .cta-post a { font-size: 20px; }

  .figure-accent {
    position: absolute; left: 645px; top: 323px; width: 44px; height: 143px;
    border-radius: 20px 20px 6px 6px;
    background: linear-gradient(180deg, #ff6cf4, #e03ce0);
    box-shadow: 0 0 10px rgba(255, 90, 240, .8);
  }
</style>
</head>
<body>
  <main class="email">
    <header class="email-header">
      <div class="brand-name">velvetlistings-uk.com</div>
      <div class="brand-tagline">The Escort Directory</div>
    </header>

    <section class="email-body">
      <div class="profile-frame">
        <div class="profile-photo" role="img" aria-label="Profile photo of the advertiser"></div>
      </div>

      <h1 class="profile-name">Mara, 22</h1>
      <p class="profile-location">Birmingham City Centre Escort</p>
      <p class="profile-bio">
        New to Birmingham - Hello Guys, my name is Mara,<br>
        I am from Sweeden. My pictures are 100% genuine,<br>
        I am a glamour model. Call me Kisses Mara XXX XXX<br>
        I am warm, fun and discreet x Book ahead
      </p>

      <p class="cta cta-browse">Take a look <a href="#">@www.velvetlistings-uk.com</a></p>
      <p class="cta cta-post">Post an ad <a href="#">@www.velvetlistings-uk.com/post/add</a></p>

      <div class="figure-accent" role="img" aria-label="Glowing pink silhouette of a standing woman"></div>
    </section>
  </main>
</body>
</html>
```